Business Card Design Project

Prime Swift Tasks- http:primeswifttasks.com./janetcorley

Industry/Entity Type

Business

Contact Information for Business Card

Well it could be a pretty color like a glossy pink look business type very Job related

```html
<!DOCTYPE html>
<html lang="en">
<head>
<meta charset="utf-8">
<title>Prime Swift Tasks – Business Card</title>
<link rel="stylesheet" href="https://fonts.googleapis.com/css2?family=Roboto+Condensed:wght@400;700&family=Roboto:wght@400&display=swap">
<style>
  :root {
    --backdrop: #2e2e30;
    --card-red: #b42844;
    --card-red-deep: #9e1f39;
    --card-ink: #ffffff;
    --rule: rgba(255, 255, 255, 0.75);
  }
  * { margin: 0; padding: 0; box-sizing: border-box; }
  html, body {
    width: 1200px;
    height: 507px;
    overflow: hidden;
    background: var(--backdrop);
  }
  .stage {
    width: 1200px;
    height: 507px;
    display: flex;
    align-items: center;
    justify-content: center;
  }
  .business-card {
    position: relative;
    width: 700px;
    height: 400px;
    border-radius: 38px;
    background: linear-gradient(160deg, var(--card-red) 0%, var(--card-red-deep) 100%);
    color: var(--card-ink);
  }
  .identity {
    position: absolute;
    right: 360px;
    top: 186px;
    text-align: left;
  }
  .identity__name {
    font-family: "Roboto Condensed", Arial, sans-serif;
    font-weight: 700;
    font-size: 28px;
    letter-spacing: 0.5px;
    text-transform: uppercase;
    line-height: 1;
  }
  .identity__role {
    font-family: "Roboto Condensed", Arial, sans-serif;
    font-weight: 400;
    font-size: 19px;
    letter-spacing: 0.6px;
    text-transform: uppercase;
    margin-top: 6px;
    line-height: 1;
  }
  .divider {
    position: absolute;
    left: 365px;
    top: 148px;
    width: 1.5px;
    height: 110px;
    background: var(--rule);
  }
  .contact-list {
    position: absolute;
    left: 392px;
    top: 136px;
    list-style: none;
    font-family: "Roboto", Arial, sans-serif;
    font-size: 17px;
    line-height: 1;
  }
  .contact-list__item {
    display: flex;
    align-items: center;
    gap: 12px;
    height: 28px;
  }
  .contact-list__icon {
    width: 17px;
    height: 17px;
    flex: none;
  }
</style>
</head>
<body>
  <main class="stage">
    <article class="business-card" aria-label="Prime Swift Tasks business card">
      <div class="identity">
        <h1 class="identity__name">Janet Corley</h1>
        <p class="identity__role">Managing Director</p>
      </div>

      <span class="divider" aria-hidden="true"></span>

      <ul class="contact-list">
        <li class="contact-list__item">
          <svg class="contact-list__icon" viewBox="0 0 20 20" aria-hidden="true">
            <path fill="#fff" d="M2 7c0-2 3.5-4 8-4s8 2 8 4v1.5h-4V7c-1-.6-2.4-1-4-1s-3 .4-4 1v1.5H2z"/>
            <path fill="#fff" d="M5 9.5h10l2 7H3z"/>
            <circle cx="10" cy="13" r="2" fill="#b42844"/>
          </svg>
          <span>41 62 508 7394</span>
        </li>
        <li class="contact-list__item">
          <svg class="contact-list__icon" viewBox="0 0 20 20" aria-hidden="true">
            <rect x="1.5" y="4" width="17" height="12" fill="#fff"/>
            <path d="M1.5 4.5l8.5 6.5 8.5-6.5" fill="none" stroke="#b42844" stroke-width="1.6"/>
          </svg>
          <span>janet@primeswifttasks.com</span>
        </li>
        <li class="contact-list__item">
          <svg class="contact-list__icon" viewBox="0 0 20 20" aria-hidden="true">
            <g fill="none" stroke="#fff" stroke-width="1.6">
              <circle cx="10" cy="10" r="8"/>
              <ellipse cx="10" cy="10" rx="3.5" ry="8"/>
              <path d="M2 10h16M3.5 6h13M3.5 14h13"/>
            </g>
          </svg>
          <span>www.primeswifttasks.com</span>
        </li>
      </ul>
    </article>
  </main>
</body>
</html>
```